WWW.VELTRONA.IT BUSINNES CARD

WE NEED A BUSINESS CARD . I HAVE A COMPANY IN ITALY NR 1 IN HAIR MEDICAL CARE AN HAIR REPLECEMENT . IN CARD I NEED WRITE WEB ADDRESS, MAIL , ADDRESS, TELEPHONE NUMBER , AND NAME
IN THE BACK SIDE I NEED MY DOCTOR LOGO .
MY WEB SITE IS WWW.VELTRONA.IT
Updates

Target Market(s)

CONSUMER B2C

Industry/Entity Type

Hair And Beauty

Contact Information for Business Card

I WANT A MEDICAL BUSINESS CARD.

Font styles to use
Other font styles liked:
• VERDANA

Colors
33a6d7
3176b5
85abd2
aedbee
eaf1f7
ffffff

Requirements
Must have
• I NEED MY LOGO AND LOGO OF DR VELTRONA

```html
<!DOCTYPE html>
<html lang="it">
<head>
<meta charset="utf-8">
<title>Veltrona – Biglietto da visita</title>
<link href="https://fonts.googleapis.com/css2?family=Open+Sans:wght@400;700&display=swap" rel="stylesheet">
<style>
  :root {
    --navy: #0a5597;
    --sky: #2db4e8;
    --card: #ffffff;
    --page: #fdfdfd;
    --edge: #e6e6e6;
    --hair-brown: #7a4a2a;
    --hair-light: #e9c7ad;
  }
  * { margin: 0; padding: 0; box-sizing: border-box; }
  html, body {
    width: 1200px; height: 1200px; overflow: hidden;
    background: var(--page);
    font-family: "Open Sans", Verdana, sans-serif;
  }
  .canvas { position: relative; width: 1200px; height: 1200px; }
  .card {
    position: absolute; left: 396px; width: 408px; height: 264px;
    background: var(--card); border: 1px solid var(--edge); overflow: hidden;
  }
  .card--front { top: 241px; }
  .card--back { top: 645px; }
  .band { position: absolute; left: 0; width: 100%; }
  .band--navy-top { top: 0; height: 14px; background: var(--navy); }
  .band--sky-top { top: 16px; height: 9px; background: var(--sky); }
  .band--sky-bottom { bottom: 14px; height: 8px; background: var(--sky); }
  .band--navy-bottom { bottom: 0; height: 12px; background: var(--navy); }

  .brand { position: absolute; text-align: center; }
  .brand__name { color: var(--navy); font-weight: 700; line-height: 1; letter-spacing: -0.5px; }
  .brand__tagline { color: var(--navy); font-weight: 400; white-space: nowrap; }

  .card--front .brand { left: 98px; top: 86px; width: 212px; }
  .card--front .brand__name { font-size: 42px; }
  .card--front .brand__tagline { font-size: 10.5px; margin-top: 8px; }

  .card--back .brand { left: 254px; top: 40px; width: 120px; }
  .card--back .brand__name { font-size: 23px; }
  .card--back .brand__tagline { font-size: 6px; margin-top: 3px; }

  .mascot {
    position: absolute; left: 22px; top: 32px; width: 114px; height: 204px;
    background: linear-gradient(180deg, var(--hair-brown) 0%, #a9714a 60%, var(--hair-light) 100%);
    border-radius: 6px;
  }
  .contact {
    position: absolute; left: 181px; top: 126px; height: 110px;
    border-left: 1.5px solid var(--sky); padding-left: 13px; padding-top: 3px;
  }
  .contact__line { color: var(--sky); font-size: 11.5px; line-height: 21px; }
</style>
</head>
<body>
<div class="canvas">
  <section class="card card--front">
    <div class="band band--navy-top"></div>
    <div class="band band--sky-top"></div>
    <div class="brand">
      <div class="brand__name">Veltrona</div>
      <div class="brand__tagline">CURA E REINTEGRAZIONE DEI CAPELLI</div>
    </div>
    <div class="band band--sky-bottom"></div>
    <div class="band band--navy-bottom"></div>
  </section>

  <section class="card card--back">
    <div class="band band--navy-top"></div>
    <div class="band band--sky-top"></div>
    <div class="mascot" role="img" aria-label="Mascotte del dottore Veltrona: un capello sorridente in camice con la scritta dr. Veltrona"></div>
    <div class="brand">
      <div class="brand__name">Veltrona</div>
      <div class="brand__tagline">CURA E REINTEGRAZIONE DEI CAPELLI</div>
    </div>
    <div class="contact">
      <p class="contact__line">Name</p>
      <p class="contact__line">Add</p>
      <p class="contact__line">Tel</p>
      <p class="contact__line">Web Add</p>
      <p class="contact__line">Mail Add</p>
    </div>
    <div class="band band--sky-bottom"></div>
    <div class="band band--navy-bottom"></div>
  </section>
</div>
</body>
</html>
```